Design Business Card MAPLE WREN MOWING

We have attached a copy of our Logo, we like a business card designed with logo and mobile phone number on one side that stands out maybe gloss and on the other side it can have the services we do small picture of our logo name number, I have attached an idea to this that I have seen online, this is a business owned by a woman so we like pinks black and navy
Our logo is attached in pdf
Target Market(s)
Home owners that need lawns mowed
Industry/Entity Type
Lawns and gardens
Contact Information for Business Card
Logo business Owner name Deborah Finch mobile number 0491627504
Font styles to use
Look and feel
Each slider illustrates characteristics of the customer's brand and the style your logo design should communicate.

```html
<!DOCTYPE html>
<html lang="en">
<head>
<meta charset="utf-8">
<title>Maple Wren Mowing – Business Card</title>
<link href="https://fonts.googleapis.com/css2?family=Montserrat:wght@600;700;800&family=Great+Vibes&display=swap" rel="stylesheet">
<style>
  :root {
    --bg: #2b2b2b;
    --card-black: #111111;
    --card-white: #ffffff;
    --pink: #e0399e;
    --green: #3bb34a;
    --ink: #111111;
    --white: #ffffff;
    --grass-light: #8fd14f;
  }
  * { box-sizing: border-box; margin: 0; padding: 0; }
  html, body { width: 1200px; height: 875px; overflow: hidden; }
  body {
    background: var(--bg);
    font-family: "Montserrat", sans-serif;
    position: relative;
  }
  .card {
    position: absolute;
    width: 540px;
    height: 309px;
    border-radius: 18px;
    overflow: hidden;
    top: 283px;
  }
  /* Front */
  .card-front {
    left: 40px;
    background: linear-gradient(160deg, #1e1e1e, var(--card-black));
    display: flex;
    flex-direction: column;
    align-items: center;
    justify-content: center;
    gap: 26px;
  }
  .brand {
    display: flex;
    align-items: center;
    gap: 14px;
  }
  .brand-dot {
    width: 34px; height: 34px;
    border-radius: 50%;
    background: var(--pink);
  }
  .brand-name {
    font-weight: 800;
    color: var(--pink);
    font-size: 30px;
    letter-spacing: 1px;
  }
  .front-phone {
    color: var(--white);
    font-weight: 700;
    font-size: 30px;
    letter-spacing: 4px;
  }
  /* Back */
  .card-back {
    left: 620px;
    background: var(--card-white);
  }
  .back-brand {
    position: absolute;
    top: 22px; right: 70px;
    font-weight: 800;
    color: var(--pink);
    font-size: 17px;
    letter-spacing: .5px;
  }
  .bee-art {
    position: absolute;
    top: 16px; right: 18px;
    width: 40px; height: 34px;
    border-radius: 50%;
    background: radial-gradient(circle, #f3b23a, #e9e9e9);
  }
  .mower-art {
    position: absolute;
    top: 62px; right: 24px;
    width: 270px; height: 120px;
    border-radius: 14px;
    background: linear-gradient(135deg, #e66ab8, #2a2a2a);
  }
  .grass-art {
    position: absolute;
    bottom: 0; right: 0;
    width: 150px; height: 70px;
    border-top-left-radius: 70px;
    background: linear-gradient(180deg, var(--grass-light), var(--green));
  }
  .owner {
    position: absolute;
    left: 24px; top: 78px;
  }
  .owner-name {
    font-family: "Great Vibes", cursive;
    color: var(--pink);
    font-size: 40px;
    line-height: 1;
  }
  .owner-phone {
    color: var(--green);
    font-weight: 700;
    font-size: 24px;
    letter-spacing: 1px;
  }
  .fields {
    position: absolute;
    left: 24px; top: 170px;
    width: 320px;
    font-size: 10px;
    font-weight: 700;
    color: var(--ink);
  }
  .field-row { display: flex; gap: 6px; margin-bottom: 8px; }
  .field-line { flex: 1; border-bottom: 1.5px dotted var(--ink); }
  .services {
    position: absolute;
    left: 24px; bottom: 18px;
    font-size: 10.5px;
    font-weight: 700;
    color: var(--pink);
    line-height: 1.5;
  }
  .services .sep { color: var(--green); margin: 0 3px; }
</style>
</head>
<body>
  <section class="card card-front">
    <div class="brand">
      <span class="brand-dot"></span>
      <span class="brand-name">MAPLE WREN MOWING</span>
    </div>
    <div class="front-phone">0491627504</div>
  </section>

  <section class="card card-back">
    <div class="back-brand">MAPLE WREN MOWING</div>
    <div class="bee-art" role="img" aria-label="Small bee illustration"></div>
    <div class="mower-art" role="img" aria-label="Pink lawn mower illustration"></div>
    <div class="grass-art" role="img" aria-label="Green grass tuft illustration"></div>

    <div class="owner">
      <div class="owner-name">Deborah Finch</div>
      <div class="owner-phone">0491627504</div>
    </div>

    <div class="fields">
      <div class="field-row"><span>A GIFT TO :</span><span class="field-line"></span><span>NO :</span><span class="field-line" style="flex:.5"></span></div>
      <div class="field-row"><span>DATE :</span><span class="field-line"></span></div>
      <div class="field-row"><span>VALUED AT :</span><span class="field-line"></span></div>
      <div class="field-row"><span>FROM :</span><span class="field-line"></span></div>
    </div>

    <div class="services">
      <div>MOWING<span class="sep">●</span>PLANTING<span class="sep">●</span>MULCHING<span class="sep">●</span>CLEAN-UP</div>
      <div>FERTILIZING<span class="sep">●</span>WEEDING<span class="sep">●</span>TRIMMING<span class="sep">●</span>SODDING</div>
    </div>
  </section>
</body>
</html>
```